PowerPoint Design Project Oil and Gas Company

For background please visit www.brastonhollowpower.com for our trial web site, attached is a brief write-up on the firm with our logo and styling on our name. Use the colors you see on the web page and write-up

Our audience is technical oil and gas engineers

I need a master slide as well as the five slides completed. Don't spend too much time on the master slide because the design elements, logo and colors have already been chosen so stay with them.

I need it all done by April 8th. I will be chosing quickly and will look to form a long-term relationship for upcoming presentations, collateral sales materials, finishing the web site, etc.

I would appreciate if your first language was English and if you had a technical background or experience with technical issues, preferably oil and gas.

Oil And Gas

```html
<!DOCTYPE html>
<html lang="en">
<head>
<meta charset="utf-8">
<title>Produce Water Treatment</title>
<link rel="stylesheet" href="https://fonts.googleapis.com/css2?family=Tinos:wght@400;700&family=Arimo:wght@400;700&display=swap">
<style>
  :root {
    --olive: #7f9c3a;
    --olive-dark: #5d7a22;
    --pipe-green: #6f8f33;
    --leaf: #92d050;
    --power-red: #c00000;
    --frac-red: #a52a2a;
    --gas-purple: #5e4a8a;
    --gas-box: #8c6fb8;
    --water-blue: #4a86d6;
    --wt-blue: #3d7ddb;
    --gen-grey: #6b6b6b;
    --orange: #f7913d;
    --bar-grey: #8c8c8c;
    --ghost-grey: #d7d7d7;
    --ghost-blue: #dbe8f8;
    --ink: #404040;
    --footer-black: #0d0d0d;
  }
  html, body { margin: 0; padding: 0; overflow: hidden; background: #ffffff; }
  .slide { width: 1200px; height: 900px; position: relative; overflow: hidden; background: #ffffff; }
  .slide svg { display: block; width: 1200px; height: 900px; }
  .slide-title { font-family: "Tinos", "Times New Roman", serif; font-weight: 700; font-size: 45px; fill: var(--olive); }
  .label { font-family: "Arimo", Arial, sans-serif; font-weight: 700; font-size: 13px; fill: #ffffff; }
  .label-dark { font-family: "Arimo", Arial, sans-serif; font-weight: 700; font-size: 13px; fill: var(--ink); }
  .label-power { font-family: "Arimo", Arial, sans-serif; font-weight: 700; font-size: 16px; fill: var(--power-red); }
  .brand-name { font-family: "Tinos", "Times New Roman", serif; font-size: 30px; fill: #ffffff; }
  .pipe { fill: none; stroke-linejoin: miter; }
  .power { stroke: var(--power-red); stroke-width: 2.5; }
  .oil { stroke: var(--pipe-green); stroke-width: 7; }
  .gas { stroke: var(--gas-purple); stroke-width: 7; }
  .water { stroke: var(--water-blue); stroke-width: 6; }
  .heat { stroke: var(--gen-grey); stroke-width: 7; }
  .brine { stroke: var(--leaf); stroke-width: 7; }
  .frac { stroke: var(--frac-red); stroke-width: 7; }
  .ghost-red { stroke: #eaa0a0; stroke-width: 3; stroke-dasharray: 10 6; }
  .ghost-purple { stroke: #c8c0e0; stroke-width: 4; stroke-dasharray: 10 6; }
  .ghost-blue { stroke: #c4daf5; stroke-width: 4; stroke-dasharray: 10 6; }
  .ghost-heat { stroke: #a8a8a8; stroke-width: 6; }
  .ghost-edge { stroke: #9a9a9a; stroke-width: 1; stroke-dasharray: 4 3; }
</style>
</head>
<body>
<main class="slide">
<svg viewBox="0 0 960 720" xmlns="http://www.w3.org/2000/svg">
  <defs>
    <linearGradient id="bar-grad" x1="0" y1="0" x2="0" y2="1">
      <stop offset="0" stop-color="#b5b5b5"/><stop offset="1" stop-color="#7a7a7a"/>
    </linearGradient>
    <linearGradient id="mark-grad" x1="0" y1="0" x2="1" y2="1">
      <stop offset="0" stop-color="#c7e27a"/><stop offset="1" stop-color="#6f9a1e"/>
    </linearGradient>
    <linearGradient id="footer-grad" x1="0" y1="0" x2="0" y2="1">
      <stop offset="0" stop-color="#9cc94a"/><stop offset="1" stop-color="#6b9a22"/>
    </linearGradient>
    <linearGradient id="brine-grad" x1="0" y1="0" x2="1" y2="0">
      <stop offset="0" stop-color="#7fc23a"/><stop offset="0.5" stop-color="#a6dd66"/><stop offset="1" stop-color="#6fae2e"/>
    </linearGradient>
    <linearGradient id="frac-grad" x1="0" y1="0" x2="1" y2="0">
      <stop offset="0" stop-color="#c0504d"/><stop offset="0.5" stop-color="#de7a76"/><stop offset="1" stop-color="#b03e3b"/>
    </linearGradient>
    <marker id="arrow-green" markerWidth="4" markerHeight="4" refX="1" refY="2" orient="auto"><path d="M0,0 L4,2 L0,4 Z" fill="#6f8f33"/></marker>
    <marker id="arrow-leaf" markerWidth="4" markerHeight="4" refX="1" refY="2" orient="auto"><path d="M0,0 L4,2 L0,4 Z" fill="#92d050"/></marker>
    <marker id="arrow-frac" markerWidth="4" markerHeight="4" refX="1" refY="2" orient="auto"><path d="M0,0 L4,2 L0,4 Z" fill="#a52a2a"/></marker>
  </defs>

  <!-- Header -->
  <rect class="header-mark" x="30" y="42" width="72" height="72" fill="url(#mark-grad)"/>
  <rect class="header-bar" x="104" y="72" width="840" height="12" fill="url(#bar-grad)"/>
  <text class="slide-title" x="935" y="57" text-anchor="end">Produce Water Treatment</text>

  <!-- Future expansion (dashed) -->
  <g class="expansion">
    <path class="pipe ghost-red" d="M372,176 H452 M372,263 H452"/>
    <path class="pipe ghost-purple" d="M437,157 V355"/>
    <path class="pipe ghost-blue" d="M573,157 V355"/>
    <path class="pipe ghost-heat" d="M545,176 H595 M545,263 H595"/>
    <g fill="#dcdcdc"><rect class="ghost-edge" x="452" y="140" width="85" height="60"/><polygon class="ghost-edge" points="452,140 462,130 547,130 537,140"/><polygon class="ghost-edge" fill="#c4c4c4" points="537,140 547,130 547,190 537,200"/></g>
    <g fill="#dcdcdc"><rect class="ghost-edge" x="452" y="235" width="85" height="60"/><polygon class="ghost-edge" points="452,235 462,225 547,225 537,235"/><polygon class="ghost-edge" fill="#c4c4c4" points="537,235 547,225 547,285 537,295"/></g>
    <g fill="#e3edf9"><rect class="ghost-edge" x="595" y="140" width="85" height="60" stroke="#8fb3e0"/><polygon class="ghost-edge" stroke="#8fb3e0" points="595,140 605,130 690,130 680,140"/><polygon class="ghost-edge" stroke="#8fb3e0" fill="#cfe0f5" points="680,140 690,130 690,190 680,200"/></g>
    <g fill="#e3edf9"><rect class="ghost-edge" x="595" y="235" width="85" height="60" stroke="#8fb3e0"/><polygon class="ghost-edge" stroke="#8fb3e0" points="595,235 605,225 690,225 680,235"/><polygon class="ghost-edge" stroke="#8fb3e0" fill="#cfe0f5" points="680,235 690,225 690,285 680,295"/></g>
  </g>

  <!-- Power network -->
  <path class="pipe power" d="M75,208 H40 V148 H372 V440 M40,208 V585 M40,280 H75 M40,355 H75 M40,428 H75 M40,500 H75 M40,578 H75"/>
  <path class="pipe power" d="M372,312 H500 V328 M372,430 H500 V436 M262,512 V398 H372"/>
  <path class="pipe power" d="M545,343 H595 M545,452 H595"/>
  <text class="label-power" x="234" y="166">Power</text>

  <!-- Wells to separator -->
  <path class="pipe oil" d="M120,198 H178 V578 M130,280 H178 M130,352 H178 M130,428 H178 M130,500 H178 M130,578 H178 M178,545 H212"/>
  <g class="wells" fill="#7fa83a">
    <rect role="img" aria-label="pump jack" x="70" y="162" width="60" height="58"/>
    <rect role="img" aria-label="pump jack" x="70" y="238" width="60" height="58"/>
    <rect role="img" aria-label="pump jack" x="70" y="314" width="60" height="58"/>
    <rect role="img" aria-label="pump jack" x="70" y="390" width="60" height="58"/>
    <rect role="img" aria-label="pump jack" x="70" y="466" width="60" height="58"/>
    <rect role="img" aria-label="pump jack" x="70" y="542" width="60" height="58"/>
  </g>

  <!-- Midstream -->
  <path class="pipe oil" d="M305,568 H905" marker-end="url(#arrow-green)"/>
  <text class="label-dark" x="330" y="590">0.1</text>
  <text class="label-dark" x="525" y="590">Midstream Pipeline/ Truck Transport</text>

  <!-- Gas -->
  <path class="pipe gas" d="M305,530 H372 V490"/>
  <path class="pipe gas" d="M418,464 H437 V355 H456 M437,464 H456"/>
  <text class="label-dark" x="346" y="518">Gas</text>
  <text class="label-dark" transform="translate(430,392) rotate(-90)">Gas</text>

  <!-- Produced water -->
  <path class="pipe water" d="M305,548 H578 V355 H595 M578,462 H595"/>
  <text class="label-dark" x="400" y="538">Produced Water</text>

  <!-- Waste heat -->
  <path class="pipe heat" d="M545,376 H595 M545,485 H595"/>
  <text class="label-dark" x="552" y="498">Waste</text>
  <text class="label-dark" x="558" y="515">Heat</text>

  <!-- Outputs -->
  <path class="pipe brine" d="M690,330 H742 M690,460 H708 V370 H742"/>
  <path class="pipe frac" d="M690,355 H725 V435 H742"/>
  <path class="pipe brine" d="M845,333 H905" marker-end="url(#arrow-leaf)"/>
  <path class="pipe frac" d="M845,472 H905" marker-end="url(#arrow-frac)"/>
  <text class="label-dark" x="856" y="361">To Drillings/</text>
  <text class="label-dark" x="856" y="380">Completion</text>
  <text class="label-dark" x="856" y="399">Market</text>
  <text class="label-dark" x="856" y="500">To Frac</text>
  <text class="label-dark" x="856" y="519">Market</text>

  <!-- Units -->
  <g class="unit separator">
    <rect x="210" y="514" width="88" height="70" fill="var(--orange)"/>
    <polygon points="210,514 218,506 306,506 298,514" fill="#fab27a"/>
    <polygon points="298,514 306,506 306,576 298,584" fill="#d9762a"/>
    <text class="label" x="254" y="542" text-anchor="middle">Oil/ Water</text>
    <text class="label" x="254" y="560" text-anchor="middle">Separator</text>
  </g>
  <g class="unit gas-treatment">
    <rect x="330" y="446" width="82" height="46" fill="var(--gas-box)"/>
    <polygon points="330,446 338,438 420,438 412,446" fill="#ab95cf"/>
    <polygon points="412,446 420,438 420,484 412,492" fill="#6e559a"/>
    <text class="label" x="371" y="465" text-anchor="middle">Gas</text>
    <text class="label" x="371" y="483" text-anchor="middle">Treatment</text>
  </g>
  <g class="unit generator">
    <rect x="456" y="334" width="82" height="50" fill="var(--gen-grey)"/>
    <polygon points="456,334 464,326 546,326 538,334" fill="#8a8a8a"/>
    <polygon points="538,334 546,326 546,376 538,384" fill="#4f4f4f"/>
    <text class="label" x="497" y="371" text-anchor="middle">Generator</text>
  </g>
  <g class="unit generator">
    <rect x="456" y="442" width="82" height="50" fill="var(--gen-grey)"/>
    <polygon points="456,442 464,434 546,434 538,442" fill="#8a8a8a"/>
    <polygon points="538,442 546,434 546,484 538,492" fill="#4f4f4f"/>
    <text class="label" x="497" y="479" text-anchor="middle">Generator</text>
  </g>
  <g class="unit water-treatment">
    <rect x="595" y="322" width="86" height="68" fill="var(--wt-blue)"/>
    <polygon points="595,322 603,314 689,314 681,322" fill="#6fa0e6"/>
    <polygon points="681,322 689,314 689,382 681,390" fill="#2b63b5"/>
    <text class="label" x="636" y="352" text-anchor="middle">Water</text>
    <text class="label" x="636" y="370" text-anchor="middle">Treatment</text>
  </g>
  <g class="unit water-treatment">
    <rect x="595" y="428" width="86" height="68" fill="var(--wt-blue)"/>
    <polygon points="595,428 603,420 689,420 681,428" fill="#6fa0e6"/>
    <polygon points="681,428 689,420 689,488 681,496" fill="#2b63b5"/>
    <text class="label" x="636" y="458" text-anchor="middle">Water</text>
    <text class="label" x="636" y="476" text-anchor="middle">Treatment</text>
  </g>

  <!-- Tanks -->
  <g class="tank brine-tank">
    <rect x="742" y="312" width="103" height="68" fill="url(#brine-grad)"/>
    <ellipse cx="793.5" cy="380" rx="51.5" ry="12" fill="#78b836"/>
    <ellipse cx="793.5" cy="312" rx="51.5" ry="12" fill="#b9e584"/>
    <text class="label" x="793" y="360" text-anchor="middle">Brine</text>
  </g>
  <g class="tank frac-tank">
    <rect x="742" y="426" width="103" height="70" fill="url(#frac-grad)"/>
    <ellipse cx="793.5" cy="496" rx="51.5" ry="12" fill="#b5433f"/>
    <ellipse cx="793.5" cy="426" rx="51.5" ry="12" fill="#e79a96"/>
    <text class="label" x="793" y="463" text-anchor="middle">Frac</text>
    <text class="label" x="793" y="481" text-anchor="middle">Water</text>
  </g>

  <!-- Footer -->
  <rect class="footer-rule" x="0" y="632" width="960" height="14" fill="url(#bar-grad)"/>
  <rect class="footer-band" x="0" y="646" width="485" height="74" fill="url(#footer-grad)"/>
  <rect class="footer-brand" x="485" y="646" width="475" height="74" fill="var(--footer-black)"/>
  <rect x="600" y="669" width="24" height="24" fill="var(--olive)"/>
  <text class="brand-name" x="638" y="692">Braston Hollow Power</text>
</svg>
</main>
</body>
</html>
```